Business Card Design Project

Please create a custom business card for Silverpine Golf Academy. The logo is attached to this brief.

Colours could be based on Blue, black, red, or white color. Colors like orange, green, purple, pink are not preferable.

Here is the link to the logo project : http://jobs.brieflantern.com/job.aspx?id=413057

Questions can be posted on the Discussion Board.

```html
<!DOCTYPE html>
<html lang="en">
<head>
<meta charset="utf-8">
<title>Silverpine Golf Academy – Business Card</title>
<link rel="stylesheet" href="https://fonts.googleapis.com/css2?family=Open+Sans:wght@400;600;700&display=swap">
<style>
  :root {
    --stage: #d9d9d9;
    --crimson: #9b161b;
    --crimson-deep: #85111a;
    --ink: #1a1a1a;
    --paper: #ffffff;
    --charcoal: #1e1e1e;
  }
  * { box-sizing: border-box; margin: 0; padding: 0; }
  html, body {
    width: 1200px; height: 787px; overflow: hidden;
    background: var(--stage);
    font-family: "Open Sans", Arial, sans-serif;
  }
  .stage { position: relative; width: 1200px; height: 787px; }

  .card {
    position: absolute; width: 560px; height: 320px;
    box-shadow: 0 6px 18px rgba(0,0,0,.25);
    overflow: hidden;
  }

  /* Front */
  .card--front { left: 590px; top: 60px; background: var(--crimson); }
  .card--front .brand {
    position: absolute; right: 44px; bottom: 70px;
    display: flex; align-items: center; gap: 12px;
    color: var(--paper);
  }
  .brand__dot {
    width: 46px; height: 46px; border-radius: 50%;
    background: currentColor; flex: none;
  }
  .brand__name {
    font-weight: 600; font-size: 30px; line-height: 1.05;
  }

  /* Back */
  .card--back { left: 50px; top: 410px; background: var(--paper); }
  .card--back .brand {
    position: absolute; right: 36px; top: 30px;
    color: var(--crimson);
    display: flex; align-items: center; gap: 10px;
  }
  .card--back .brand__dot { width: 36px; height: 36px; }
  .card--back .brand__name { font-size: 24px; }

  .person { position: absolute; left: 36px; top: 122px; right: 36px; }
  .person__row { display: flex; align-items: center; gap: 8px; }
  .person__name { color: var(--crimson); font-weight: 700; font-size: 17px; white-space: nowrap; }
  .person__rule { flex: 1; height: 2px; background: var(--ink); }
  .person__title { font-size: 11px; color: var(--ink); margin-top: 2px; }

  .contacts { position: absolute; left: 30px; top: 180px; list-style: none; }
  .contacts li {
    display: flex; align-items: center; gap: 8px;
    font-size: 12px; font-weight: 600; color: var(--ink); line-height: 17px;
  }
  .contacts svg { width: 11px; height: 11px; fill: var(--crimson); flex: none; }

  .address {
    position: absolute; right: 36px; top: 186px;
    text-align: right; font-size: 12px; font-weight: 600; line-height: 18px; color: var(--ink);
    font-style: normal;
  }

  .band { position: absolute; left: 0; bottom: 0; width: 560px; height: 46px; }
</style>
</head>
<body>
<main class="stage">

  <section class="card card--front" aria-label="Business card front">
    <div class="brand">
      <span class="brand__dot"></span>
      <span class="brand__name">Silverpine Golf<br>Academy</span>
    </div>
  </section>

  <section class="card card--back" aria-label="Business card back">
    <div class="brand">
      <span class="brand__dot"></span>
      <span class="brand__name">Silverpine Golf<br>Academy</span>
    </div>

    <div class="person">
      <div class="person__row">
        <span class="person__name">Owen Hartley</span>
        <span class="person__rule"></span>
      </div>
      <div class="person__title">Managing Director</div>
    </div>

    <ul class="contacts">
      <li><svg viewBox="0 0 12 12"><path d="M2.5 1 4.5 1 5.3 3.6 4 4.6Q5 7 7.4 8L8.4 6.7 11 7.5 11 9.5Q10 11 8.5 11 1 9.5 1 3.5 1 2 2.5 1Z"/></svg>+1 555 014 2290</li>
      <li><svg viewBox="0 0 12 12"><path d="M3 0H9V12H3ZM4 1.5V9.5H8V1.5Z"/></svg>+1 555 018 7731</li>
      <li><svg viewBox="0 0 12 12"><path d="M0 2H12V10H0ZM1 3 6 6.5 11 3Z"/></svg>owenhartley@postmail.com</li>
      <li><svg viewBox="0 0 12 12"><path d="M0 1H12V9H7V10.5H9V11.5H3V10.5H5V9H0ZM1 2V8H11V2Z"/></svg>www.silverpinegolf.com</li>
    </ul>

    <address class="address">
      Unit 4,<br>Larch Road,<br>Fernvale, OR 97411
    </address>

    <svg class="band" viewBox="0 0 560 46" preserveAspectRatio="none" aria-hidden="true">
      <polygon points="0,8 386,8 374,46 0,46" fill="var(--crimson)"/>
      <polygon points="398,8 560,8 560,46 386,46" fill="var(--charcoal)"/>
    </svg>
  </section>

</main>
</body>
</html>
```